Meadowlark Learning Growth Partners (MLGP)

This is a professional business card. Logo and picture are a must on the front of the card. I am an educational consultant. I have been consulting for the past three years for a company. I am now opening my own company. My goal for my consulting company is to eventually consult all over America.

Target Market(s)

Educators, schools, professionals

Industry/Entity Type

Consulting

Contact Information for Business Card

Picture/logo on front, simple modern design

Font styles to use
Serif

Colors
85abd2
0355a3
3176b5
cedeed

Requirements
Must have
• picture, logo,
• Odessa Pruitt, Ed.S
• address 5073 Cormorant ridge Dr. Nashville, TN 37940
• Cell:616-555-0148
• Office: 629-555-0172
• www.Mlgpedu.example
• pruittodessa@mailbox.example

```html
<!DOCTYPE html>
<html lang="en">
<head>
<meta charset="utf-8">
<title>Meadowlark Learning Growth Partners – Business Card</title>
<link rel="stylesheet" href="https://fonts.googleapis.com/css2?family=Lexend:wght@600;700&family=Roboto:wght@400&family=Roboto+Condensed:wght@700&display=swap">
<style>
  :root {
    --backdrop: #2b2b2b;
    --card-white: #f2f2f2;
    --navy: #0b3a78;
    --navy-deep: #06326f;
    --band: #0a3a7d;
    --text-grey: #444a52;
    --white: #ffffff;
    --photo-top: #d9dde2;
    --photo-bottom: #5b6470;
  }
  * { margin: 0; padding: 0; box-sizing: border-box; }
  html, body { width: 1200px; height: 960px; overflow: hidden; }
  body { background: var(--backdrop); position: relative; font-family: "Roboto", Arial, sans-serif; }

  .card { position: absolute; width: 600px; height: 342px; border-radius: 18px; overflow: hidden; }

  /* front */
  .card-front { left: 314px; top: 113px; background: var(--card-white); }
  .card-front .bottom-band { position: absolute; left: 0; right: 0; bottom: 0; height: 12px; background: var(--band); }

  .brand-mark { position: absolute; left: 40px; top: 112px; font-family: "Lexend", Arial, sans-serif; font-weight: 700; font-size: 30px; color: var(--navy); letter-spacing: 1px; line-height: 1; }
  .brand-divider { position: absolute; left: 136px; top: 50px; width: 2px; height: 92px; background: var(--navy); }
  .company-name { position: absolute; left: 152px; top: 48px; font-family: "Lexend", Arial, sans-serif; font-weight: 600; font-size: 19.5px; line-height: 24.5px; color: var(--navy); }

  .address { position: absolute; left: 39px; top: 175px; font-size: 14px; line-height: 18px; color: var(--text-grey); }
  .contact-list { position: absolute; left: 39px; top: 223px; list-style: none; }
  .contact-list li { display: flex; align-items: center; height: 19px; font-size: 14px; color: var(--text-grey); }
  .contact-list svg { width: 14px; height: 14px; margin-right: 9px; fill: var(--navy); flex: none; }

  .portrait { position: absolute; left: 381px; top: 88px; width: 131px; height: 168px; border-radius: 12px; background: linear-gradient(180deg, var(--photo-top), var(--photo-bottom)); }
  .person-name { position: absolute; left: 300px; width: 292px; top: 271px; text-align: center; font-family: "Roboto Condensed", Arial, sans-serif; font-weight: 700; font-size: 22px; color: var(--navy); }

  /* back */
  .card-back { left: 311px; top: 472px; background: var(--navy-deep); }
  .back-mark { position: absolute; left: 0; right: 0; top: 178px; text-align: center; font-family: "Lexend", Arial, sans-serif; font-weight: 700; font-size: 50px; line-height: 1; color: var(--white); letter-spacing: 3px; }
  .back-url { position: absolute; left: 0; right: 0; top: 279px; text-align: center; font-size: 14px; letter-spacing: 10.5px; color: var(--white); }
</style>
</head>
<body>

<section class="card card-front">
  <div class="brand-mark">MLGP</div>
  <div class="brand-divider"></div>
  <div class="company-name">Meadowlark<br>Learning<br>Growth<br>Partners</div>

  <p class="address">5073 Cormorant ridge Dr.<br>Nashville, TN 37940</p>

  <ul class="contact-list">
    <li><svg viewBox="0 0 24 24"><path d="M6.6 10.8a15.1 15.1 0 0 0 6.6 6.6l2.2-2.2a1 1 0 0 1 1-.25 11.4 11.4 0 0 0 3.6.57 1 1 0 0 1 1 1V20a1 1 0 0 1-1 1A17 17 0 0 1 3 4a1 1 0 0 1 1-1h3.5a1 1 0 0 1 1 1c0 1.25.2 2.45.57 3.57a1 1 0 0 1-.25 1z"/></svg>629-555-0172</li>
    <li><svg viewBox="0 0 24 24"><path d="M7 1h10a2 2 0 0 1 2 2v18a2 2 0 0 1-2 2H7a2 2 0 0 1-2-2V3a2 2 0 0 1 2-2zm0 3v14h10V4zm5 15.2a1 1 0 1 0 0 2 1 1 0 0 0 0-2z"/></svg>616-555-0148</li>
    <li><svg viewBox="0 0 24 24"><path d="M2 5h20v14H2zm2 2v.4l8 5 8-5V7zm0 2.8V17h16V9.8l-8 5z"/></svg>pruittodessa@mailbox.example</li>
    <li><svg viewBox="0 0 24 24"><path d="M12 2a10 10 0 1 0 0 20 10 10 0 0 0 0-20zm-1 17.9A8 8 0 0 1 4.2 10.5L9 15.3v1a2 2 0 0 0 2 2zm6.9-2.5A2 2 0 0 0 16 16h-1v-3a1 1 0 0 0-1-1H8v-2h2a1 1 0 0 0 1-1V7h2a2 2 0 0 0 2-2v-.4a8 8 0 0 1 2.9 12.8z"/></svg>www.Mlgpedu.example</li>
  </ul>

  <div class="portrait" role="img" aria-label="Portrait photograph of Odessa Pruitt"></div>
  <h1 class="person-name">ODESSA PRUITT, ED.S</h1>

  <div class="bottom-band"></div>
</section>

<section class="card card-back">
  <div class="back-mark">MLGP</div>
  <p class="back-url">www.Mlgpedu.example</p>
</section>

</body>
</html>
```